New Design for calculator landing page

I need an original design created for a calculator application on a website.
-It needs to incorporate colors and them from the main website (tolvesa.org).
-Base calculator on a design similar, but not exact as wqn.fotu.com/calculator.php
-Incorporate the company's logo and the arrow design from the logo in the overall layout (once again this can be found on tolvesa.org.

Number of Pages Required

2 page

Requirements
Must have
• Two Designs Needed:
• -1st) Design with the base calculator design before all of the variables are entered
• -2nd) Design after the variables are entered and the slider comes out
• Use wqn.fotu.com/calculator.php for reference. Notice that after you fill in the different variables, the calculator expands out. The 2nd design needs to be the same for our calculator.
• -Make sure KOLVE's contact email and phone number are at the bottom
• Phone: 318.557.2946
• Email: info@tolvesa.org
Should not have
• Don't work about any of the actual text in the calculator. That will be added in by the programmers. I just need the layout and design. (the only text that should be added is the email and phone number at the bottom)

```html
<!DOCTYPE html>
<html lang="en">
<head>
<meta charset="utf-8">
<title>Restraint Length Calculator</title>
<link href="https://fonts.googleapis.com/css2?family=Open+Sans:wght@400;600;700&display=swap" rel="stylesheet">
<style>
:root{
  --green:#6cb33f;
  --blue:#2fa3dc;
  --ink:#2b2f33;
  --muted:#555b60;
  --field:#e4e4e4;
  --panel:#f4f4f4;
  --white:#ffffff;
  --scene-a:#d9dbdc;
  --scene-b:#bfc2c4;
}
*{box-sizing:border-box;margin:0;padding:0}
html,body{width:871px;height:1200px;overflow:hidden;background:var(--white);font-family:"Open Sans",sans-serif;color:var(--ink)}
.screen{position:absolute;left:28px;width:816px;overflow:hidden}
.screen--start{top:28px;height:530px}
.screen--expanded{top:585px;height:582px}
.backdrop{position:absolute;inset:0;background:linear-gradient(100deg,var(--scene-b) 0%,var(--scene-a) 35%,#e8e9ea 55%,var(--scene-b) 100%)}
.brand{position:absolute;top:14px;left:0;width:100%;text-align:center}
.brand-name{font-size:26px;font-weight:600;color:var(--ink);letter-spacing:.5px;line-height:1}
.brand-sub{font-size:7px;font-weight:700;color:var(--ink);margin-top:3px}
.title{position:absolute;top:72px;left:0;width:100%;text-align:center;font-size:29px;font-weight:600;color:var(--blue)}
.card{position:absolute;top:116px;left:98px;width:621px;background:var(--white)}
.screen--start .card{height:320px}
.screen--expanded .card{height:380px}
.card-head{position:relative;height:64px;background:var(--green);color:var(--white)}
.head-label{position:absolute;top:13px;font-size:10px}
.head-input{position:absolute;top:29px;width:146px;height:22px;background:var(--white)}
.notes{position:absolute;top:36px;font-size:7.5px;text-decoration:underline;color:var(--white)}
.circle-btn{position:absolute;top:29px;width:22px;height:22px}
.pager{position:absolute;top:36px;left:541px;font-size:7.5px}
.form{position:absolute;top:64px;left:0;width:310px;bottom:0}
.field{position:absolute;width:136px}
.field label{display:block;font-size:9.5px;color:var(--ink);height:15px}
.field label i{display:inline-block;width:7px;height:7px;border-radius:50%;background:#8a8f93;margin-left:3px;vertical-align:0}
.select{position:relative;height:22px;background:var(--field);font-size:7.5px;line-height:22px;padding-left:11px}
.select::after{content:"";position:absolute;right:9px;top:9px;border:3.5px solid transparent;border-top:4px solid #555}
.preview{position:absolute;top:64px;left:310px;right:0;bottom:0;background:var(--panel)}
.preview-mark{position:absolute;top:108px;left:94px;font-size:22px;font-weight:600;color:#dcdcdc}
.diagram{position:absolute;top:85px;left:16px;width:280px;height:80px;background:linear-gradient(180deg,#e6e6e6,#d3d3d3);border-radius:2px}
.partner{position:absolute;top:258px;left:78px;font-size:20px;font-weight:700;color:#8d8f91;letter-spacing:1px}
.contact{position:absolute;left:0;width:100%;text-align:center;font-size:9px;color:var(--ink)}
.page-tag{position:absolute;right:10px;font-size:8px;color:var(--ink)}
</style>
</head>
<body>

<section class="screen screen--start">
  <div class="backdrop" role="img" aria-label="Muted photograph of large ductile iron pipes in a plant"></div>
  <div class="brand"><div class="brand-name">kolve</div><div class="brand-sub">Kolve Pipe Research Association</div></div>
  <h1 class="title">Restraint Length Calculator</h1>
  <div class="card">
    <div class="card-head">
      <span class="head-label" style="left:12px">Project Name</span>
      <span class="head-input" style="left:12px"></span>
      <span class="notes" style="left:164px">Notes</span>
      <span class="head-label" style="left:221px">Site Name</span>
      <span class="head-input" style="left:221px"></span>
      <span class="notes" style="left:373px">Notes</span>
      <svg class="circle-btn" style="left:429px" viewBox="0 0 22 22"><circle cx="11" cy="11" r="10" fill="#fff" opacity=".35"/><circle cx="11" cy="11" r="7.5" fill="#fff"/><path d="M11 7v8M7 11h8" stroke="#6cb33f" stroke-width="2"/></svg>
      <svg class="circle-btn" style="left:456px" viewBox="0 0 22 22"><circle cx="11" cy="11" r="10" fill="#fff" opacity=".35"/><circle cx="11" cy="11" r="7.5" fill="#fff"/><path d="M8.5 8.5l5 5M13.5 8.5l-5 5" stroke="#6cb33f" stroke-width="2"/></svg>
      <svg class="circle-btn" style="left:513px" viewBox="0 0 22 22"><circle cx="11" cy="11" r="10" fill="#fff"/><path d="M15 11H7M10 7.5L6.5 11 10 14.5" stroke="#6cb33f" stroke-width="2.2" fill="none"/></svg>
      <span class="pager">Item 1 of 1</span>
      <svg class="circle-btn" style="left:584px" viewBox="0 0 22 22"><circle cx="11" cy="11" r="10" fill="#fff"/><path d="M7 11h8M12 7.5l3.5 3.5-3.5 3.5" stroke="#6cb33f" stroke-width="2.2" fill="none"/></svg>
    </div>
    <div class="form">
      <div class="field" style="top:15px;left:12px"><label>Pipe Material<i></i></label><div class="select"></div></div>
      <div class="field" style="top:15px;left:161px"><label>Soil Type<i></i></label><div class="select"></div></div>
      <div class="field" style="top:75px;left:12px"><label>Safety Factor<i></i></label><div class="select"></div></div>
      <div class="field" style="top:75px;left:161px"><label>Trench Type<i></i></label><div class="select"></div></div>
      <div class="field" style="top:135px;left:12px"><label>Depth of Bury (ft.)<i></i></label><div class="select"></div></div>
      <div class="field" style="top:135px;left:161px"><label>Test Pressure<i></i></label><div class="select"></div></div>
      <div class="field" style="top:195px;left:12px"><label>Fitting Type<i></i></label><div class="select"></div></div>
    </div>
    <div class="preview"><span class="preview-mark">kolve</span></div>
  </div>
  <p class="contact" style="top:459px">KOLVE's contact infos : Phone: 318.557.2946 &nbsp;|&nbsp; Email: info@tolvesa.org</p>
  <p class="contact" style="top:479px">Copyright © 2018 Kolve Pipe Research Association. &nbsp;All rights reserved.</p>
  <span class="page-tag" style="top:502px">M2</span>
</section>

<section class="screen screen--expanded">
  <div class="backdrop" role="img" aria-label="Muted photograph of large ductile iron pipes in a plant"></div>
  <div class="brand"><div class="brand-name">kolve</div><div class="brand-sub">Kolve Pipe Research Association</div></div>
  <h1 class="title">Restraint Length Calculator</h1>
  <div class="card">
    <div class="card-head">
      <span class="head-label" style="left:12px">Project Name</span>
      <span class="head-input" style="left:12px"></span>
      <span class="notes" style="left:164px">Notes</span>
      <span class="head-label" style="left:221px">Site Name</span>
      <span class="head-input" style="left:221px"></span>
      <span class="notes" style="left:373px">Notes</span>
      <svg class="circle-btn" style="left:429px" viewBox="0 0 22 22"><circle cx="11" cy="11" r="10" fill="#fff" opacity=".35"/><circle cx="11" cy="11" r="7.5" fill="#fff"/><path d="M11 7v8M7 11h8" stroke="#6cb33f" stroke-width="2"/></svg>
      <svg class="circle-btn" style="left:456px" viewBox="0 0 22 22"><circle cx="11" cy="11" r="10" fill="#fff" opacity=".35"/><circle cx="11" cy="11" r="7.5" fill="#fff"/><path d="M8.5 8.5l5 5M13.5 8.5l-5 5" stroke="#6cb33f" stroke-width="2"/></svg>
      <svg class="circle-btn" style="left:513px" viewBox="0 0 22 22"><circle cx="11" cy="11" r="10" fill="#fff"/><path d="M15 11H7M10 7.5L6.5 11 10 14.5" stroke="#6cb33f" stroke-width="2.2" fill="none"/></svg>
      <span class="pager">Item 1 of 1</span>
      <svg class="circle-btn" style="left:584px" viewBox="0 0 22 22"><circle cx="11" cy="11" r="10" fill="#fff"/><path d="M7 11h8M12 7.5l3.5 3.5-3.5 3.5" stroke="#6cb33f" stroke-width="2.2" fill="none"/></svg>
    </div>
    <div class="form">
      <div class="field" style="top:15px;left:12px"><label>Pipe Material<i></i></label><div class="select">PVC</div></div>
      <div class="field" style="top:15px;left:161px"><label>Soil Type<i></i></label><div class="select">SW</div></div>
      <div class="field" style="top:75px;left:12px"><label>Safety Factor<i></i></label><div class="select">2.0 to 1</div></div>
      <div class="field" style="top:75px;left:161px"><label>Trench Type<i></i></label><div class="select">4</div></div>
      <div class="field" style="top:135px;left:12px"><label>Depth of Bury (ft.)<i></i></label><div class="select">2.5</div></div>
      <div class="field" style="top:135px;left:161px"><label>Test Pressure<i></i></label><div class="select">60</div></div>
      <div class="field" style="top:195px;left:12px"><label>Fitting Type<i></i></label><div class="select">Vertical Offset Sym Ret</div></div>
      <div class="field" style="top:195px;left:161px"><label>Nominal Size<i></i></label><div class="select"></div></div>
      <div class="field" style="top:255px;left:12px"><label>Bend Angle<i></i></label><div class="select"></div></div>
      <div class="field" style="top:255px;left:161px"><label>Low Side Depth (ft.)<i></i></label><div class="select"></div></div>
    </div>
    <div class="preview">
      <div class="diagram" role="img" aria-label="Technical drawing of a vertical offset pipe run with restrained joints"></div>
      <span class="partner">NORVIK IRON</span>
    </div>
  </div>
  <p class="contact" style="top:525px">KOLVE's contact infos : Phone: 318.557.2946 &nbsp;|&nbsp; Email: info@tolvesa.org</p>
  <p class="contact" style="top:545px">Copyright © 2018 Kolve Pipe Research Association. &nbsp;All rights reserved.</p>
  <span class="page-tag" style="top:562px">M2</span>
</section>

</body>
</html>
```